TheHarborKeyway.com (Luxury Business Card Design)

I’m looking for assistance with design. I have a clear vision in mind, but I need help translating it into a properly formatted file for print.
Ideally, I’d like to work directly with a designer to communicate my vision and finalize the design in the correct vector format required for submission to a printing company. I already have some examples I've created just need someone with design experience to help me do the finishing touches

Target Market(s)

Real Estate

Industry/Entity Type

Real Estate

Contact Information for Business Card

the name of the company, QR code, my The harbor keyway email. Owner/founder title.

Font styles to use
Decorative
Script

Requirements
Must have
• vector for printing company
Nice to have
• I am set on a black and gold design, and will be using a gold foiling. QR code to be done in a gold foiling or inlay.
Should not have
• wild colors I want black and gold, please see my pdf examples.

```html
<!DOCTYPE html>
<html lang="en">
<head>
<meta charset="utf-8">
<title>The Harbor Keyway — Business Card</title>
<link href="https://fonts.googleapis.com/css2?family=Cinzel:wght@500;700&display=swap" rel="stylesheet">
<style>
  :root{
    --backdrop:#f2cc9f;
    --card:#080808;
    --gold:#e2b022;
    --gold-light:#fff07a;
    --gold-deep:#b87a0c;
    --gold-band:linear-gradient(90deg,#f6c21a 0%,#ffe45a 35%,#fff27e 60%,#f9d23a 80%,#e8b018 100%);
    --gold-band-rich:linear-gradient(90deg,#ffe33a 0%,#fff27a 20%,#c98a12 55%,#f2b820 75%,#ffe13a 100%);
    --gold-text:linear-gradient(180deg,#fff07a 0%,#f2c62a 45%,#c98a10 100%);
    --line-grey:#c8c8c8;
  }
  *{box-sizing:border-box;margin:0;padding:0}
  html,body{width:1200px;height:1200px;overflow:hidden}
  body{background:var(--backdrop);position:relative;font-family:"Cinzel",serif}
  .card{position:absolute;left:233px;width:729px;height:417px;background:var(--card);overflow:hidden}
  .card--front{top:125px}
  .card--back{top:600px}
  .band{position:absolute;height:18px;background:var(--gold-band)}
  .band--rich{background:var(--gold-band-rich)}
  .flourish{position:absolute;border-radius:16px;
    background:radial-gradient(ellipse at center,rgba(232,184,34,.55) 0%,rgba(200,140,16,.25) 55%,rgba(0,0,0,0) 75%)}
  .emblem{position:absolute;border-radius:50%;border:3px solid var(--gold)}
  .company-name{position:absolute;left:0;right:0;text-align:center;color:var(--gold);
    font-weight:700;letter-spacing:1px;white-space:nowrap;line-height:1}
  .holder{position:absolute;right:67px;top:88px;text-align:right;line-height:1}
  .holder__name{font-size:33px;font-weight:700;letter-spacing:1px;
    background:var(--gold-text);-webkit-background-clip:text;background-clip:text;color:transparent}
  .holder__title{font-size:18px;font-weight:700;color:var(--gold);margin-top:2px}
  .contact{position:absolute;left:475px;top:168px;list-style:none}
  .contact li{display:flex;align-items:center;height:32px;margin-bottom:6px}
  .contact__icon{width:32px;height:32px;border:2px solid var(--line-grey);display:flex;align-items:center;justify-content:center;flex:none}
  .contact__icon svg{width:20px;height:20px;fill:none;stroke:var(--line-grey);stroke-width:1.6}
  .contact__text{margin-left:9px;font-size:11.5px;font-weight:700;color:var(--gold)}
</style>
</head>
<body>

<section class="card card--front">
  <div class="emblem" style="left:275px;top:75px;width:180px;height:180px"></div>
  <div class="flourish" role="img" aria-label="Gold ornamental flourish framing the emblem" style="left:270px;top:65px;width:190px;height:190px;border-radius:50%;opacity:.6"></div>
  <p class="company-name" style="top:280px;font-size:38px">The Harbor Keyway</p>
  <div class="band" style="left:0;top:370px;width:497px"></div>
  <div class="flourish" role="img" aria-label="Gold scroll flourish ornament" style="left:522px;top:364px;width:157px;height:32px"></div>
  <div class="band" style="left:702px;top:370px;width:27px"></div>
</section>

<section class="card card--back">
  <div class="band" style="left:0;top:32px;width:27px"></div>
  <div class="flourish" role="img" aria-label="Gold scroll flourish ornament" style="left:50px;top:25px;width:157px;height:33px"></div>
  <div class="band band--rich" style="left:233px;top:32px;width:496px"></div>

  <div class="emblem" style="left:151px;top:118px;width:138px;height:138px"></div>
  <div class="flourish" role="img" aria-label="Gold ornamental flourish framing the emblem" style="left:146px;top:112px;width:148px;height:150px;border-radius:50%;opacity:.6"></div>
  <p class="company-name" style="top:282px;left:43px;right:auto;width:356px;font-size:29px">The Harbor Keyway</p>

  <div class="holder">
    <p class="holder__name">YOUR NAME</p>
    <p class="holder__title">Owner</p>
  </div>

  <ul class="contact">
    <li>
      <span class="contact__icon"><svg viewBox="0 0 20 20"><rect x="2" y="5" width="16" height="10"/><path d="M2 5l8 6 8-6"/></svg></span>
      <span class="contact__text">Your@Email.com</span>
    </li>
    <li>
      <span class="contact__icon"><svg viewBox="0 0 20 20"><path d="M5 3l3 3-2 2c1 2 3 4 5 5l2-2 3 3-2 3C8 17 3 12 2 5z"/></svg></span>
      <span class="contact__text">+0123-456789</span>
    </li>
    <li>
      <span class="contact__icon"><svg viewBox="0 0 20 20"><path d="M3 9l7-6 7 6M5 8v9h10V8"/><rect x="8" y="12" width="4" height="5"/></svg></span>
      <span class="contact__text">Your Address</span>
    </li>
    <li>
      <span class="contact__icon"><svg viewBox="0 0 20 20"><circle cx="10" cy="10" r="7.5"/><ellipse cx="10" cy="10" rx="3.5" ry="7.5"/><path d="M2.5 10h15M4 6h12M4 14h12"/></svg></span>
      <span class="contact__text">www.yourwebsite.com</span>
    </li>
  </ul>

  <div class="band band--rich" style="left:0;top:370px;width:497px"></div>
  <div class="flourish" role="img" aria-label="Gold scroll flourish ornament" style="left:522px;top:362px;width:157px;height:34px"></div>
  <div class="band" style="left:702px;top:370px;width:27px"></div>
</section>

</body>
</html>
```